Notepads for Marketing pieces-BOLD design

Looking for notepads for marketing pieces with logo, phone number, and website. Maybe something faded in background. Looking for bold and different

```html
<!DOCTYPE html>
<html lang="en">
<head>
<meta charset="utf-8">
<title>Vitalis Care Notepad</title>
<link href="https://fonts.googleapis.com/css2?family=Poppins:wght@600;800&family=Oswald:wght@300;400&family=Michroma&display=swap" rel="stylesheet">
<style>
  :root {
    --backdrop: #e6e6e6;
    --ink: #050505;
    --brand-red: #e4141b;
    --bright-white: #ffffff;
    --soft-white: #ececec;
    --photo-light: #8c8c8c;
    --photo-mid: #6a6a6a;
    --photo-dark: #3c3c3c;
  }
  html, body {
    margin: 0;
    padding: 0;
    width: 1200px;
    height: 1001px;
    overflow: hidden;
    background: var(--backdrop);
  }
  .notepad {
    position: absolute;
    left: 275px;
    top: 50px;
    width: 650px;
    height: 900px;
    background: var(--ink);
    overflow: hidden;
  }
  .notepad-art {
    position: absolute;
    inset: 0;
    display: block;
  }
  .brand {
    position: absolute;
    top: 70px;
    left: 0;
    width: 100%;
    text-align: center;
  }
  .brand-name {
    margin: 0;
    font-family: "Poppins", sans-serif;
    font-weight: 800;
    font-size: 54px;
    line-height: 1;
    letter-spacing: 1px;
    color: var(--bright-white);
  }
  .brand-tagline {
    margin: 18px 0 0;
    font-family: "Poppins", sans-serif;
    font-weight: 600;
    font-size: 12.5px;
    letter-spacing: 1px;
    color: var(--bright-white);
  }
  .services {
    position: absolute;
    top: 612px;
    left: 0;
    width: 100%;
    display: flex;
    justify-content: center;
    align-items: stretch;
    margin: 0;
    padding: 0;
    list-style: none;
  }
  .service {
    font-family: "Oswald", sans-serif;
    font-weight: 400;
    font-size: 29px;
    line-height: 1.08;
    letter-spacing: 2px;
    color: var(--soft-white);
    text-align: center;
    padding: 0 14px;
  }
  .service + .service {
    border-left: 3px solid var(--brand-red);
  }
  .website {
    position: absolute;
    top: 834px;
    left: 0;
    width: 100%;
    margin: 0;
    text-align: center;
    font-family: "Michroma", sans-serif;
    font-size: 24px;
    line-height: 1;
    letter-spacing: 4px;
    color: var(--brand-red);
  }
</style>
</head>
<body>
  <main class="notepad">
    <svg class="notepad-art" width="650" height="900" viewBox="0 0 650 900">
      <defs>
        <radialGradient id="photoTone" cx="0.3" cy="0.35" r="0.9">
          <stop offset="0" stop-color="var(--photo-light)"/>
          <stop offset="0.55" stop-color="var(--photo-mid)"/>
          <stop offset="1" stop-color="var(--photo-dark)"/>
        </radialGradient>
      </defs>
      <rect class="care-photo" x="0" y="200" width="650" height="620" fill="url(#photoTone)" role="img" aria-label="Black and white photo of a masked nurse checking an elderly patient's finger with a pulse oximeter at a table"/>

      <path class="top-band-red" d="M0 0 H650 V440 C560 300 300 240 0 255 Z" fill="var(--brand-red)"/>
      <path class="top-band-dark" d="M0 0 H650 V335 C500 265 250 225 0 238 Z" fill="var(--ink)"/>
      <path class="top-band-white" d="M0 0 H650 V312 C500 245 250 210 0 224 Z" fill="var(--bright-white)"/>
      <path class="top-panel" d="M0 0 H650 V290 C500 222 250 188 0 203 Z" fill="var(--ink)"/>

      <path class="bottom-band-red" d="M0 780 C200 725 450 695 650 705 V900 H0 Z" fill="var(--brand-red)"/>
      <path class="bottom-arc" d="M0 800 C220 710 470 680 650 720 V900 H0 Z" fill="var(--ink)"/>
      <path class="bottom-band-white" d="M0 840 C240 765 470 735 650 775 V900 H0 Z" fill="var(--bright-white)"/>
      <path class="bottom-panel" d="M0 860 C240 790 470 760 650 800 V900 H0 Z" fill="var(--ink)"/>
    </svg>

    <header class="brand">
      <h1 class="brand-name">VITALIS CARE</h1>
      <p class="brand-tagline">HOME HEALTH | MEDICAL STAFFING | OUTPATIENT THERAPY</p>
    </header>

    <ul class="services">
      <li class="service">IN-HOME<br>CARE</li>
      <li class="service">IN-HOME<br>THERAPY</li>
      <li class="service">OUTPATIENT<br>THERAPY</li>
    </ul>

    <p class="website">VITALISCARE.ORG</p>
  </main>
</body>
</html>
```